CareLumen business cards

We need a business card design that we could customize as needed for employees. We will need space for Name, Title, 1-2 phone numbers and email address.

We are a Pharmacy Benefits Management (PBM) company for hospice agencies and beginning a nationwide expansion. Attached is a vector file of our logo.

Cards can be single or double sided.

```html
<!DOCTYPE html>
<html lang="en">
<head>
<meta charset="utf-8">
<title>CareLumen business cards</title>
<link rel="stylesheet" href="https://fonts.googleapis.com/css2?family=Questrial&display=swap">
<style>
  :root {
    --stage: #2b2b2d;
    --paper: #ffffff;
    --green: #8da03a;
    --blue: #1e6a95;
    --navy: #1f5a7a;
    --text-blue: #245d80;
    --gap: #ffffff;
  }
  * { box-sizing: border-box; margin: 0; padding: 0; }
  html, body {
    width: 1200px; height: 900px; overflow: hidden;
    background: var(--stage);
    font-family: "Questrial", "Century Gothic", sans-serif;
  }
  .canvas { position: relative; width: 1200px; height: 900px; }
  .card {
    position: absolute; left: 280px; width: 640px; height: 366px;
    background: var(--paper); overflow: hidden;
    box-shadow: 0 12px 30px rgba(0,0,0,0.45);
  }
  .card--back { top: 44px; }
  .card--front { top: 480px; }

  /* back side */
  .back-field { position: absolute; inset: 0; }
  .back-wordmark {
    position: absolute; left: 50%; top: 50%;
    transform: translate(-50%, -50%);
    width: 300px; height: 120px; background: var(--paper);
    display: flex; align-items: center; justify-content: center;
    color: var(--blue); font-size: 44px; letter-spacing: -0.5px;
  }

  /* front side */
  .brand {
    position: absolute; left: 44px; top: 46px;
    display: flex; align-items: center; gap: 14px;
  }
  .brand-square { width: 46px; height: 46px; background: var(--green); border-radius: 6px; }
  .brand-name { color: var(--text-blue); font-size: 46px; letter-spacing: -0.5px; }

  .person { position: absolute; left: 150px; top: 140px; }
  .person-name { color: var(--text-blue); font-size: 24px; }
  .person-title { color: var(--text-blue); font-size: 15px; margin-top: 4px; }

  .contact { position: absolute; left: 150px; top: 214px; list-style: none; }
  .contact li { color: var(--text-blue); font-size: 16px; line-height: 22px; }
  .contact .label { color: var(--green); display: inline-block; width: 16px; }

  .address {
    position: absolute; right: 40px; top: 132px;
    color: var(--text-blue); font-size: 14px; line-height: 20px; text-align: left;
  }

  .footer-green { position: absolute; left: 0; bottom: 0; width: 176px; height: 62px; background: var(--green); }
  .footer-blue { position: absolute; left: 182px; right: 0; bottom: 0; height: 62px; background: var(--navy); }
  .footer-blue-step { position: absolute; left: 440px; right: 0; bottom: 62px; height: 56px; background: var(--navy); }
</style>
</head>
<body>
<main class="canvas">

  <section class="card card--back" aria-label="Card back">
    <svg class="back-field" width="640" height="366" viewBox="0 0 640 366" aria-hidden="true">
      <rect x="0" y="0" width="640" height="366" fill="var(--paper)"/>
      <rect x="0" y="0" width="316" height="180" fill="var(--blue)"/>
      <rect x="0" y="186" width="316" height="180" fill="var(--green)"/>
      <rect x="324" y="0" width="316" height="180" fill="var(--green)"/>
      <rect x="324" y="186" width="316" height="180" fill="var(--blue)"/>
    </svg>
    <div class="back-wordmark">CareLumen</div>
  </section>

  <section class="card card--front" aria-label="Card front">
    <div class="brand">
      <span class="brand-square"></span>
      <span class="brand-name">CareLumen</span>
    </div>

    <div class="person">
      <p class="person-name">Daniel Marlow</p>
      <p class="person-title">managing director</p>
    </div>

    <ul class="contact">
      <li><span class="label">p</span> 5550 142 367</li>
      <li><span class="label">m</span> 5550 298 714</li>
      <li><span class="label">e</span> dmarlow@carelumen.com</li>
    </ul>

    <address class="address" style="font-style:normal">
      48 Maple Lane<br>
      Brookfield, Ohio 44403<br>
      www.carelumen.com
    </address>

    <div class="footer-green"></div>
    <div class="footer-blue"></div>
  </section>

</main>
</body>
</html>
```